Aircraft maintenance buisness card

I am an aircraft mechanic looking for a personal buisness card . I would like my name and a title of Aircraft Maintenance Manager . I would like a suttle picture of an aircraft and helicopter .

elegant and professional wtih my contact .

My name should be on the car and Aircraft Maintenance Manager under with my contact infor below .

i have attached some pictures but i am open to other pics and ideas . I would like a airliner or private jet and a helicopter in the picture . The Images should be suttle and not the main idea . I also uploaded a picture of a jet engine which is cool . Be creative and i will work with you to finalize something .
Updates

Project Deadline Extended
Reason: Looking for more variations . Very good so far but looiking for a bit more styles and i uploaded my logo that i purchased . Please use my logo and be creative with it . I like some variations of black card with maybe some pictures that i uploaded but i am open to ideas . Be creative and i will work with you .

Project Deadline Extended
Reason: Looking for more designs and variations . Not yet satisfied with the designs i have gotten .

Industry/Entity Type

Aviation

Contact Information for Business Card

Aircraft Maintenance Manager

Font styles to use
Serif

Colors

Designer to choose colors to be used in the design.

Requirements
Must have
• An aviation related Logo if possible incorporated in the card possibly
• My name
• Tobias Marven Ellery
• 482 Pellow Ave.
• Brenwick , NH
• 07519
• Email: Tmskyworks@quillmail.net
Nice to have
• Suttle Backround of a Private Jet or Airliner and a Helicopter .

```html
<!DOCTYPE html>
<html lang="en">
<head>
<meta charset="utf-8">
<title>Tobias Marven Ellery – Business Card</title>
<link rel="stylesheet" href="https://fonts.googleapis.com/css2?family=PT+Sans:wght@400;700&display=swap">
<style>
  :root {
    --backdrop: #2b2b2b;
    --card: #111112;
    --card-edge: #1c1c1d;
    --accent: #f5a01e;
    --ink: #e9e9e9;
    --rule: #3a3a3a;
  }
  * { margin: 0; padding: 0; box-sizing: border-box; }
  html, body {
    width: 1200px;
    height: 900px;
    overflow: hidden;
    background: var(--backdrop);
    font-family: "PT Sans", sans-serif;
  }
  .stage {
    position: relative;
    width: 1200px;
    height: 900px;
    display: flex;
    align-items: center;
    justify-content: center;
    gap: 60px;
  }
  .card {
    width: 500px;
    height: 286px;
    background: var(--card);
    border-radius: 16px;
    box-shadow: 0 0 0 1px var(--card-edge);
    position: relative;
    overflow: hidden;
  }
  .brand {
    display: flex;
    align-items: center;
    gap: 10px;
  }
  .brand-dot {
    width: 14px;
    height: 14px;
    border-radius: 50%;
    background: var(--accent);
    flex: none;
  }
  .brand-name {
    color: var(--ink);
    font-weight: 700;
    letter-spacing: 1px;
    white-space: nowrap;
  }
  .card-front .brand {
    position: absolute;
    left: 34px;
    top: 128px;
  }
  .card-front .brand-name { font-size: 24px; }
  .details {
    position: absolute;
    left: 262px;
    top: 58px;
    padding-left: 12px;
    border-left: 1px solid var(--rule);
    color: var(--ink);
  }
  .person-name {
    color: var(--accent);
    font-weight: 700;
    font-size: 16px;
    line-height: 1.2;
  }
  .person-title {
    font-size: 12px;
    line-height: 1.3;
  }
  .address {
    font-size: 12px;
    margin-top: 28px;
    white-space: nowrap;
  }
  .contact-list {
    list-style: none;
    margin-top: 26px;
    font-size: 12px;
  }
  .contact-list li {
    display: flex;
    align-items: center;
    gap: 7px;
    line-height: 1.5;
  }
  .contact-list svg { width: 10px; height: 10px; flex: none; }
  .card-back {
    display: flex;
    align-items: center;
    justify-content: center;
  }
  .card-back .brand-name { font-size: 32px; }
  .card-back .brand-dot { width: 18px; height: 18px; }
</style>
</head>
<body>
<main class="stage">
  <section class="card card-front">
    <div class="brand">
      <span class="brand-dot"></span>
      <span class="brand-name">Marven Aero</span>
    </div>
    <div class="details">
      <p class="person-name">Tobias Marven Ellery</p>
      <p class="person-title">Aircraft Maintenance Manager</p>
      <p class="address">482 Pellow Ave. Brenwick , NH 07519</p>
      <ul class="contact-list">
        <li>
          <svg viewBox="0 0 10 10" aria-hidden="true"><path fill="var(--accent)" d="M2 0.5 L3.6 0.5 L4.3 2.8 L3.2 3.7 Q4.2 5.8 6.3 6.8 L7.2 5.7 L9.5 6.4 L9.5 8 Q9.5 9.5 8 9.5 Q0.5 9 0.5 2 Q0.5 0.5 2 0.5 Z"/></svg>
          <span>201 555 0148</span>
        </li>
        <li>
          <svg viewBox="0 0 10 10" aria-hidden="true"><rect x="0.5" y="2" width="9" height="6.5" fill="var(--accent)"/><path d="M0.5 2 L5 5.8 L9.5 2" fill="none" stroke="var(--card)" stroke-width="1"/></svg>
          <span>Tmskyworks@quillmail.net</span>
        </li>
      </ul>
    </div>
  </section>
  <section class="card card-back">
    <div class="brand">
      <span class="brand-dot"></span>
      <span class="brand-name">Marven Aero</span>
    </div>
  </section>
</main>
</body>
</html>
```